cartNest - a stylish trolley for apartments

We neede a simple website to sell our Trolley, for apartment use.
The colour theme is red, blask & white. Our logo is attached and this needs to be on the Home page.
The website only needs a Home Page plus 4 other pges.
In the attachment you will find a site map.

You can check out the following two sites to see what I like:
www.plinvex.example/design-showcase-inspiration/minimalist-portfolio-website/
www.brostaquill.example/inspiration/40-beautiful-web-design-portfolios/ in this site especially
Dario Pesqueta
Q L Smithy
Nine 86 Studio
Albert Crisp

And especially Lamp - I ike the simpicity of the site esp as we are only selling one product

Target Market(s)

Apartment dwellers

Industry/Entity Type

Apartment

Requirements
Must have
• This website must have 4 pages.
We need Zanto, Fundline and Quibpay portals.
Order Form for Trolley
Payment form.

```html
<!DOCTYPE html>
<html lang="en">
<head>
<meta charset="utf-8">
<title>cartNest – a stylish trolley for apartments</title>
<link rel="stylesheet" href="https://fonts.googleapis.com/css2?family=Arimo:wght@400;700&family=Playfair+Display:ital,wght@0,400;0,700;1,700&display=swap">
<style>
:root{
  --black:#050505;
  --header-top:#2a2a2a;
  --red:#b50d0d;
  --red-dark:#7a0505;
  --white:#ffffff;
  --grey-bg:#ececec;
  --text-grey:#8a8a8a;
  --text-dark:#333333;
  --hero-light:#e9e6e4;
  --hero-photo-a:#b9b2ac;
  --hero-photo-b:#7d6b62;
}
*{margin:0;padding:0;box-sizing:border-box}
html,body{width:1000px;height:1200px;overflow:hidden;background:var(--white);font-family:"Arimo",Arial,sans-serif}
.page{position:relative;width:1000px;height:1200px}

.site-header{position:absolute;left:0;top:0;width:1000px;height:171px;background:linear-gradient(var(--header-top),var(--black) 60%);border-bottom:2px solid #444}
.logo{position:absolute;left:4px;top:0;width:164px;height:168px;background:var(--white);display:flex;align-items:center;justify-content:center;gap:8px}
.logo-mark{width:18px;height:18px;background:var(--red)}
.logo-name{font-size:30px;font-weight:700;color:var(--red)}
.phone-top{position:absolute;right:10px;top:26px;display:flex;align-items:center;gap:8px;color:var(--white);font-size:20px;font-weight:700}
.main-nav a{position:absolute;top:115px;display:block;height:32px;line-height:32px;color:var(--white);text-decoration:none;font-size:19px;white-space:nowrap}
.main-nav .home{left:541px;padding:0 9px;background:linear-gradient(#d51a1a,var(--red-dark));border-radius:4px;box-shadow:0 4px 6px rgba(150,0,0,.5)}
.main-nav .about{left:675px}
.main-nav .contact{left:789px}
.main-nav .news{left:923px}

.top-strip{position:absolute;left:0;top:173px;width:1000px;height:34px;background:linear-gradient(#f4f4f4,#dcdcdc)}

.hero{position:absolute;left:0;top:209px;width:1000px;height:304px;background:linear-gradient(90deg,var(--hero-light),#d8d3cf 45%);border-top:2px solid #999;border-bottom:2px solid #999}
.hero-photo{position:absolute;left:467px;top:0;width:533px;height:100%;background:linear-gradient(120deg,var(--hero-photo-a),#a59a92 50%,var(--hero-photo-b))}
.hero-title{position:absolute;left:51px;top:116px;font-family:"Playfair Display",Georgia,serif;font-weight:400;color:#2a1a1a;line-height:1;white-space:nowrap}
.hero-title .lead{font-style:italic;font-weight:700;font-size:36px}
.hero-title .caps{font-size:37px;font-weight:400;letter-spacing:1px}
.hero-title .line2{display:block;font-size:46px;font-weight:400;margin-top:2px}

.intro{position:absolute;left:0;top:516px;width:1000px;height:137px;background:linear-gradient(#1a1a1a,var(--black));padding:12px 40px 0 17px;color:var(--text-grey);font-size:11px;line-height:17.5px;border-bottom:2px solid #444}
.intro .brand{color:var(--white);font-size:14px;font-weight:700}
.intro .brand b{color:var(--red)}
.intro a{color:var(--red);text-decoration:none}

.gallery{position:absolute;left:0;top:656px;width:1000px;height:257px;background:var(--grey-bg)}
.tab{position:absolute;height:33px;line-height:33px;padding:0 14px;background:linear-gradient(#ffffff,#d9d9d9);border-radius:5px;box-shadow:0 2px 4px rgba(0,0,0,.35);font-weight:700;font-size:17px;color:#111;white-space:nowrap}
.gallery .tab{left:7px;top:21px}
.thumbs{position:absolute;left:24px;top:72px;display:flex;gap:5px}
.thumb{width:186px;height:159px}
.thumb-1{background:linear-gradient(#8d8a84,#5d5a58)}
.thumb-2{background:linear-gradient(#a9a9a0,#77756e)}
.thumb-3{background:linear-gradient(#b1b1af,#5a5552)}
.thumb-4{background:linear-gradient(#d8d6d2,#a9a6a2)}
.thumb-5{background:linear-gradient(#8a4a3e,#d0ccc7 45%,#e8e6e3)}
.arrow{position:absolute;top:117px;width:34px;height:60px;background:rgba(230,230,230,.9);display:flex;align-items:center;justify-content:center}
.arrow-left{left:7px}
.arrow-right{right:7px}

.info{position:absolute;left:0;top:917px;width:1000px;height:228px;background:var(--white)}
.info-col{position:absolute;top:0;height:100%}
.info-col .tab{top:11px;font-size:16px;padding:0 10px}
.col-contact{left:7px;width:340px}
.col-payment{left:377px;width:300px}
.col-news{left:744px;width:250px}
.row{position:absolute;display:flex;align-items:center;gap:14px;font-size:12.5px;color:var(--text-dark);line-height:18px;white-space:nowrap}
.link-red{color:var(--red);text-decoration:underline}
.link-grey{color:#555;text-decoration:underline}
.big-phone{font-size:19px;font-weight:700;color:#111}
.pay-label{position:absolute;left:7px;top:167px;font-weight:700;font-size:12.5px;color:#111}
.pay-chips{position:absolute;left:7px;top:192px;display:flex;gap:12px}
.chip{height:20px;padding:0 5px;border:1px solid #bbb;border-radius:3px;font-size:10px;line-height:18px;color:#333;background:#f5f5f5}
.news-item{position:absolute;left:2px;width:245px;font-size:11.5px;color:#555;line-height:18px}
.news-item .date{display:flex;align-items:center;gap:8px;font-weight:700;color:#111;font-size:12px}
.read-more{position:absolute;left:0;top:200px;color:var(--red);font-size:11.5px;text-decoration:none}

.site-footer{position:absolute;left:0;top:1147px;width:1000px;height:53px;background:var(--black);border-top:3px solid #666;color:var(--white);font-size:11px;text-align:center;line-height:50px}
</style>
</head>
<body>
<div class="page">

<header class="site-header">
  <div class="logo"><span class="logo-mark"></span><span class="logo-name">cartNest</span></div>
  <div class="phone-top">
    <svg width="40" height="40" viewBox="0 0 40 40" aria-hidden="true"><rect x="6" y="18" width="28" height="18" rx="3" fill="#8a5a2a"/><path d="M4 14 Q20 4 36 14 L32 18 Q20 12 8 18Z" fill="#5a3512"/><circle cx="20" cy="27" r="5" fill="#d9b070"/></svg>
    <span>+140 55501247</span>
  </div>
  <nav class="main-nav">
    <a class="home" href="#">&#8962; Home</a>
    <a class="about" href="#">About Us</a>
    <a class="contact" href="#">Contact Us</a>
    <a class="news" href="#">News</a>
  </nav>
</header>

<div class="top-strip"></div>

<section class="hero">
  <div class="hero-photo" role="img" aria-label="Chrome luggage trolley holding a bag and suitcases beside a carpeted staircase"></div>
  <h1 class="hero-title"><span class="lead">a stylish</span> <span class="caps">TROLLEY</span><span class="line2">for apartments</span></h1>
</section>

<section class="intro">
  <p><span class="brand"><b>cart</b>Nest</span> evolved from demand!&nbsp; Apartment dwellers everywhere are calling for a solution to moving shopping, luggage and other goods from car to apartment, and vice versa. Other trolleys on the market are not versatile, they are not robust, but more importantly, they are NOT stylish! The emphasis of cartNest is on style. This trolley is stylish enough to remain in your apartment as a piece of furniture. It features a versatile flat-bed and hanger, to cope with all your transport needs.cartNest evolved from demand!&nbsp; Apartment dwellers everywhere are calling for a solution to moving shopping, luggage and other goods from car to apartment, and vice versa. Other trolleys on the market are not versatile, they are not robust, but more importantly, they are NOT stylish! The emphasis of cartNest is on style. This trolley is stylish enough to remain in your apartment as a piece of furniture. It features a versatile flat-bed and hanger, to cope with all your transport needs.<a href="#">MORE</a></p>
</section>

<section class="gallery">
  <div class="tab">Gallery</div>
  <div class="thumbs">
    <div class="thumb thumb-1" role="img" aria-label="Loading garment bags onto the trolley from a car boot"></div>
    <div class="thumb thumb-2" role="img" aria-label="Trolley beside a white car in a parking garage"></div>
    <div class="thumb thumb-3" role="img" aria-label="Trolley with red suitcase in a lift"></div>
    <div class="thumb thumb-4" role="img" aria-label="Close view of the chrome hanger rail"></div>
    <div class="thumb thumb-5" role="img" aria-label="Close view of the trolley wheels"></div>
  </div>
  <div class="arrow arrow-left"><svg width="12" height="20" viewBox="0 0 12 20"><path d="M9 2 L3 10 L9 18" stroke="#333" stroke-width="3" fill="none"/></svg></div>
  <div class="arrow arrow-right"><svg width="12" height="20" viewBox="0 0 12 20"><path d="M9 2 L3 10 L9 18" stroke="#333" stroke-width="3" fill="none"/></svg></div>
</section>

<section class="info">
  <div class="info-col col-contact">
    <div class="tab">CONTACT</div>
    <div class="row" style="left:0;top:63px">
      <svg width="28" height="32" viewBox="0 0 28 32" aria-hidden="true"><rect x="3" y="1" width="23" height="30" rx="3" fill="#2b6fb8"/><circle cx="15" cy="16" r="6" fill="none" stroke="#fff" stroke-width="2.5"/><rect x="0" y="6" width="5" height="3" fill="#888"/><rect x="0" y="15" width="5" height="3" fill="#888"/><rect x="0" y="24" width="5" height="3" fill="#888"/></svg>
      <span>Suite 210, 4870 Merrow Lane,<br>Dalton Square, Orvania</span>
    </div>
    <div class="row" style="left:0;top:117px">
      <svg width="30" height="26" viewBox="0 0 30 26" aria-hidden="true"><rect x="1" y="4" width="28" height="19" rx="2" fill="#e8eef5" stroke="#6a8ab0"/><path d="M2 5 L15 15 L28 5" stroke="#6a8ab0" stroke-width="1.5" fill="none"/></svg>
      <a class="link-red" href="#">hello@cartnest.example</a>
    </div>
    <div class="row" style="left:0;top:166px">
      <svg width="30" height="30" viewBox="0 0 30 30" aria-hidden="true"><rect width="30" height="30" rx="5" fill="#4aa23a"/><path d="M9 7 Q7 16 14 21 Q19 24 22 22 L20 18 L17 19 Q13 16 13 12 L15 10 Z" fill="#fff"/></svg>
      <span class="big-phone">+0140555019372</span>
    </div>
  </div>

  <div class="info-col col-payment">
    <div class="tab">PAYMENT</div>
    <div class="row" style="left:7px;top:64px">
      <svg width="26" height="30" viewBox="0 0 26 30" aria-hidden="true"><rect x="2" y="1" width="22" height="28" fill="#fff" stroke="#8aa"/><path d="M6 8h14M6 13h14M6 18h14M6 23h10" stroke="#7a9ac0" stroke-width="2"/></svg>
      <a class="link-red" href="#">Order form</a>
    </div>
    <div class="row" style="left:7px;top:116px">
      <svg width="26" height="30" viewBox="0 0 26 30" aria-hidden="true"><rect x="2" y="1" width="22" height="28" fill="#fff8e6" stroke="#c9a24a"/><path d="M6 8h14M6 13h14M6 18h10" stroke="#e09a2a" stroke-width="2"/></svg>
      <a class="link-grey" href="#">Payment Form</a>
    </div>
    <div class="pay-label">Payment Option</div>
    <div class="pay-chips">
      <span class="chip">Quibpay</span>
      <span class="chip">Zanto</span>
      <span class="chip">Fundline</span>
    </div>
  </div>

  <div class="info-col col-news">
    <div class="tab">NEWS</div>
    <div class="news-item" style="top:62px">
      <div class="date"><svg width="18" height="16" viewBox="0 0 18 16" aria-hidden="true"><rect x="1" y="1" width="16" height="14" fill="#fff" stroke="#5a7ab0"/><rect x="3" y="4" width="5" height="5" fill="#3a6ac0"/><path d="M10 5h5M10 8h5M3 12h12" stroke="#5a7ab0"/></svg>Date:21 july,2012</div>
      <p>Lorem Ipsum is simply dummy text of the printing and typesetting industry</p>
    </div>
    <div class="news-item" style="top:132px">
      <div class="date"><svg width="18" height="16" viewBox="0 0 18 16" aria-hidden="true"><rect x="1" y="1" width="16" height="14" fill="#fff" stroke="#5a7ab0"/><rect x="3" y="4" width="5" height="5" fill="#3a6ac0"/><path d="M10 5h5M10 8h5M3 12h12" stroke="#5a7ab0"/></svg>Date:21 july,2012</div>
      <p>Lorem Ipsum is simply dummy text of the printing and typesetting industry</p>
    </div>
    <a class="read-more" href="#">READ MORE</a>
  </div>
</section>

<footer class="site-footer">Copyright © 2011 cartNest</footer>

</div>
</body>
</html>
```